Need Bold, Hip Card for Concert Ticket Website Velvet Stubs!

Hi there! I am putting together a business/website that sells event tickets (mostly concerts, but also some sports and theater). Think PassDepot, but much smaller. The site is called Velvet Stubs. I have a new logo (attached, with black/red/white color scheme), and am looking for a modern/cool/original business card design. Note that I am thinking of having the card itself in the shape of a ticket (die cut), so you may want to keep that in mind when designing, but I'm not set on that. I'm also open to alternative card sizes, thicknesses, glossy, spot UV, etc. in order to stand out. I'm attaching a potential die cut template and a sample card using that template in case you want to work with that.
Target Market(s)
Music fans, people that like going to see live events
Industry/Entity Type
Entertainment
Contact Information for Business Card
Information that I'd like to have:
website address - www.velvetstubs-example.com
phone number: 1-833-5VELVETS (835-3887)
my name - Delia Hart
Look and feel
Each slider illustrates characteristics of the customer's brand and the style your logo design should communicate.

```html
<!DOCTYPE html>
<html lang="en">
<head>
<meta charset="utf-8">
<title>Velvet Stubs – Business Card</title>
<link rel="stylesheet" href="https://fonts.googleapis.com/css2?family=Fira+Sans:wght@400;700;800&display=swap">
<style>
  :root {
    --stage: #e8e5e1;
    --paper: #f4f4f3;
    --brand-red: #8e0a0a;
    --red-bright: #c40606;
    --red-deep: #870707;
    --ink: #0d0b0b;
    --text-grey: #555353;
    --white: #ffffff;
  }
  * { box-sizing: border-box; margin: 0; padding: 0; }
  html, body { width: 1200px; height: 960px; overflow: hidden; }
  body { background: var(--stage); position: relative; font-family: "Fira Sans", Arial, sans-serif; }

  .card { position: absolute; left: 335px; width: 530px; height: 305px; }
  .card--front { top: 165px; }
  .card--back { top: 510px; }
  .card-shape { position: absolute; inset: 0; width: 530px; height: 305px; filter: drop-shadow(0 4px 8px rgba(0,0,0,0.25)); }

  .wordmark { position: absolute; display: flex; align-items: center; gap: 10px; font-weight: 800; line-height: 0.95; text-transform: uppercase; }
  .wordmark__square { width: 38px; height: 56px; flex: none; }
  .wordmark__name { display: flex; flex-direction: column; }
  .wordmark__top { font-size: 31px; letter-spacing: 0.5px; }
  .wordmark__bottom { font-size: 23px; letter-spacing: 7px; }

  .card--front .wordmark { left: 40px; top: 110px; color: var(--brand-red); }
  .card--front .wordmark__square { background: var(--brand-red); }
  .card--back .wordmark { left: 127px; top: 115px; color: var(--white); }
  .card--back .wordmark__top { font-size: 42px; }
  .card--back .wordmark__bottom { font-size: 31px; letter-spacing: 10px; }
  .card--back .wordmark__square { width: 52px; height: 78px; background: var(--white); }

  .contact { position: absolute; left: 276px; top: 102px; }
  .contact__name { font-size: 23px; font-weight: 700; color: var(--brand-red); text-transform: uppercase; letter-spacing: 0.2px; margin-bottom: 5px; }
  .contact__line { display: flex; align-items: center; gap: 6px; font-size: 13px; color: var(--text-grey); text-transform: uppercase; line-height: 18px; }
  .contact__icon { width: 12px; height: 12px; fill: var(--brand-red); flex: none; }

  .card__website { position: absolute; left: 72px; top: 279px; font-size: 13px; color: var(--white); letter-spacing: 2.6px; text-transform: uppercase; }
</style>
</head>
<body>

<section class="card card--front" aria-label="Card front">
  <svg class="card-shape" viewBox="0 0 530 305" aria-hidden="true">
    <defs>
      <clipPath id="ticket-front">
        <path d="M30,0 H500 A30,30 0 0 0 530,30 V275 A30,30 0 0 0 500,305 H30 A30,30 0 0 0 0,275 V30 A30,30 0 0 0 30,0 Z"/>
      </clipPath>
    </defs>
    <g clip-path="url(#ticket-front)">
      <rect width="530" height="305" fill="var(--paper)"/>
      <polygon points="0,270 372,270 364,305 0,305" fill="var(--brand-red)"/>
      <polygon points="372,270 375,270 367,305 364,305" fill="var(--white)"/>
      <polygon points="377,270 530,270 530,305 369,305" fill="var(--ink)"/>
    </g>
  </svg>

  <div class="wordmark">
    <span class="wordmark__square"></span>
    <span class="wordmark__name">
      <span class="wordmark__top">Velvet</span>
      <span class="wordmark__bottom">Stubs</span>
    </span>
  </div>

  <div class="contact">
    <p class="contact__name">Delia Hart</p>
    <p class="contact__line">
      <svg class="contact__icon" viewBox="0 0 24 24" aria-hidden="true"><path d="M6.6 10.8a15.1 15.1 0 0 0 6.6 6.6l2.2-2.2c.3-.3.7-.4 1-.2 1.1.4 2.3.6 3.6.6.6 0 1 .4 1 1V20c0 .6-.4 1-1 1A17 17 0 0 1 3 4c0-.6.4-1 1-1h3.5c.6 0 1 .4 1 1 0 1.3.2 2.5.6 3.6.1.3 0 .7-.2 1z"/></svg>
      1-833-5VELVETS (835-3887)
    </p>
    <p class="contact__line">
      <svg class="contact__icon" viewBox="0 0 24 24" aria-hidden="true"><path d="M2 5h20v14H2z M2 5l10 7 10-7" fill="var(--brand-red)"/><path d="M3 6l9 6.3L21 6" fill="none" stroke="var(--paper)" stroke-width="1.8"/></svg>
      info@velvetstubs-example.com
    </p>
  </div>

  <p class="card__website">www.velvetstubs-example.com</p>
</section>

<section class="card card--back" aria-label="Card back">
  <svg class="card-shape" viewBox="0 0 530 305" aria-hidden="true">
    <defs>
      <linearGradient id="back-gradient" x1="0" y1="0" x2="1" y2="0.7">
        <stop offset="0" stop-color="var(--red-bright)"/>
        <stop offset="0.45" stop-color="var(--red-deep)"/>
        <stop offset="1" stop-color="var(--red-deep)"/>
      </linearGradient>
    </defs>
    <path d="M30,0 H500 A30,30 0 0 0 530,30 V275 A30,30 0 0 0 500,305 H30 A30,30 0 0 0 0,275 V30 A30,30 0 0 0 30,0 Z" fill="url(#back-gradient)"/>
  </svg>

  <div class="wordmark">
    <span class="wordmark__square"></span>
    <span class="wordmark__name">
      <span class="wordmark__top">Velvet</span>
      <span class="wordmark__bottom">Stubs</span>
    </span>
  </div>
</section>

</body>
</html>
```